A Freight forwarding (transportation/shipping) company requires stationary design

We need The following:
1. Letterhead
2. Letter Envelope
3. A4 Paper Envelope
4. A4 Paper Folder (One that is 2xA4 foldable size which we can open in half and we can put a paper in between)
5. A5 Paper (To be used for notes taking)

a design for a freight forwarding company named VORELTA DUNIMOR INTERNATIONAL TRANSPORTATION CO . Business Card is already designed and should follow it, the files attached help guide you in type of docs required + Logos (We are active in Sea Transportation, Truck transportation, and Air Transportation, (printed design is required with all open source files for editing - lamination accepted)

The said company is agent and sales representative of 2 other Shipping companies (whose logos, name, and website should also be mentioned on Envelopes and Folder) - Bold Wave and TQN Shipping, logos attached.

Bold Wave Shipping LLC
Dubai, United Arab Emirates
www.bwsmarine-example.com

TQN Shipping Line Ltd
London, United Kingdom
www.tqnlinex-example.com

Address is "No.7, 2nd Soltani-e-Norvand, Tehran, IR
Tel number is +98 21 55302914
Fax number is +98 21 55306631
E-Mail address is info@voreltadunimor-example.com
Website is www.voreltadunimor-example.com

```html
<!DOCTYPE html>
<html lang="en">
<head>
<meta charset="utf-8">
<title>Vorelta Dunimor – Letter Envelope</title>
<link rel="stylesheet" href="https://fonts.googleapis.com/css2?family=Poppins:wght@400;500;600&display=swap">
<style>
  :root {
    --navy: #0c3450;
    --ink: #3d4650;
    --paper: #ffffff;
    --backdrop: #e6e2dc;
    --faint: #e3e3e3;
  }
  html, body {
    margin: 0;
    padding: 0;
    width: 1200px;
    height: 1000px;
    overflow: hidden;
    background: var(--backdrop);
    font-family: "Poppins", Arial, sans-serif;
  }
  .canvas {
    position: relative;
    width: 1200px;
    height: 1000px;
  }
  .envelope {
    position: absolute;
    left: 230px;
    width: 815px;
    background: var(--paper);
    overflow: hidden;
  }
  .envelope-front { top: 128px; height: 357px; }
  .envelope-back { top: 500px; height: 355px; }

  .brand-mark {
    position: absolute;
    left: 44px;
    top: 88px;
    display: flex;
    align-items: center;
    gap: 10px;
  }
  .brand-mark .dot {
    width: 26px;
    height: 26px;
    border-radius: 50%;
    border: 2px solid var(--navy);
  }
  .brand-mark .word {
    font-size: 18px;
    font-weight: 600;
    color: var(--navy);
    letter-spacing: 0.5px;
  }
  .company-name {
    position: absolute;
    left: 44px;
    top: 206px;
    margin: 0;
    font-size: 14px;
    font-weight: 600;
    line-height: 18px;
    color: var(--navy);
    letter-spacing: 0.3px;
  }
  .contact-list {
    position: absolute;
    left: 45px;
    top: 250px;
    margin: 0;
    padding: 0;
    list-style: none;
    font-size: 12px;
    line-height: 18px;
    color: var(--ink);
  }
  .contact-list .label { color: var(--navy); }
  .address {
    position: absolute;
    right: 44px;
    top: 270px;
    margin: 0;
    font-style: normal;
    text-align: right;
    font-size: 12px;
    line-height: 18px;
    color: var(--ink);
  }
  .rule-thin {
    position: absolute;
    left: 0; right: 0;
    top: 322px;
    height: 5px;
    background: var(--navy);
  }
  .rule-band {
    position: absolute;
    left: 0; right: 0;
    top: 331px;
    height: 26px;
    background: var(--navy);
  }

  .flap { position: absolute; left: 0; top: 0; }
  .flap-mark {
    position: absolute;
    left: 0; right: 0;
    top: 28px;
    display: flex;
    justify-content: center;
    align-items: center;
    gap: 8px;
  }
  .flap-mark .dot {
    width: 16px; height: 16px;
    border-radius: 50%;
    border: 2px solid var(--paper);
  }
  .flap-mark .word {
    font-size: 13px;
    font-weight: 600;
    color: var(--paper);
    letter-spacing: 0.5px;
  }
  .ghost-mark {
    position: absolute;
    left: -40px;
    top: 140px;
    display: flex;
    align-items: center;
    gap: 18px;
  }
  .ghost-mark .dot {
    width: 210px; height: 210px;
    border-radius: 50%;
    border: 3px solid var(--faint);
  }
  .ghost-mark .word {
    font-size: 30px;
    font-weight: 600;
    color: var(--faint);
  }
</style>
</head>
<body>
<main class="canvas">
  <section class="envelope envelope-front">
    <div class="brand-mark"><span class="dot"></span><span class="word">Vorelta Dunimor</span></div>
    <h1 class="company-name">VORELTA DUNIMOR<br>INTERNATIONAL TRANSPORTATION CO</h1>
    <ul class="contact-list">
      <li><span class="label">Email:</span> info@voreltadunimor-example.com</li>
      <li><span class="label">Phone:</span> +98 21 55302914 <span class="label">| Fax:</span> +98 21 55306631</li>
      <li>www.voreltadunimor-example.com</li>
    </ul>
    <address class="address">No.7, 2nd Soltani-e-Norvand,<br>Tehran, IRAN</address>
    <div class="rule-thin"></div>
    <div class="rule-band"></div>
  </section>

  <section class="envelope envelope-back">
    <svg class="flap" width="815" height="76" viewBox="0 0 815 76" aria-hidden="true">
      <path d="M0 0 H815 V2 C800 50 770 75 730 75 H85 C45 75 15 50 0 2 Z" fill="var(--navy)"/>
    </svg>
    <div class="flap-mark"><span class="dot"></span><span class="word">Vorelta Dunimor</span></div>
    <div class="ghost-mark"><span class="dot"></span><span class="word">Vorelta Dunimor</span></div>
  </section>
</main>
</body>
</html>
```